Email Signature & Social Cover Design – Brightpath Learning Nook

I’m looking for a clean, professional email signature and a matching Social cover photo for my tutoring business, Brightpath Learning Nook.
The email signature needs to display properly across Outlook and iPhone without the image appearing as an attachment. It should include my logo and contact details and have a friendly but professional look suitable for an education business.
Details to include:
Dana Morrow
Director & Lead Tutor
Brightpath Learning Nook
hello@brightpathlearningnook.co.uk
www.brightpathlearningnook.co.uk
01632 960418
The Social cover should match the branding, feel professional and welcoming, and be optimised for desktop and mobile.

```html
<!DOCTYPE html>
<html lang="en">
<head>
<meta charset="utf-8">
<title>Brightpath Learning Nook – Email Signature &amp; Social Cover</title>
<link href="https://fonts.googleapis.com/css2?family=Poppins:wght@500;600;700;800;900&display=swap" rel="stylesheet">
<style>
  :root {
    --stage: #272727;
    --card: #ffffff;
    --brand-green: #47b169;
    --ink: #2b2b2b;
    --label: #3a3a3a;
    --white: #ffffff;
  }
  * { margin: 0; padding: 0; box-sizing: border-box; }
  html, body {
    width: 1200px; height: 240px; overflow: hidden;
    background: var(--stage);
    font-family: "Poppins", sans-serif;
  }
  .canvas { position: relative; width: 1200px; height: 240px; background: var(--stage); }

  .signature {
    position: absolute; left: 24px; top: 17px;
    width: 550px; height: 206px;
    background: var(--card);
    overflow: hidden;
  }

  .brand-name {
    position: absolute; left: 42px; top: 40px; width: 140px;
    text-align: center;
    font-weight: 800; font-size: 18px; line-height: 1.1;
    color: var(--ink);
  }

  .person-badge {
    position: absolute; left: 47px; top: 141px;
    width: 130px; height: 16px;
    background: var(--brand-green);
    border-radius: 2px;
    display: flex; align-items: center; justify-content: center;
    color: var(--white);
    font-weight: 900; font-size: 8.5px; letter-spacing: 5px;
    padding-left: 5px;
    white-space: nowrap;
  }
  .person-role {
    position: absolute; left: 32px; top: 162px; width: 160px;
    text-align: center;
    font-weight: 500; font-size: 8.4px;
    color: var(--ink);
    white-space: nowrap;
  }

  .divider {
    position: absolute; left: 216px; top: 37px;
    width: 1.5px; height: 134px;
    background: var(--brand-green);
  }

  .business-banner {
    position: absolute; left: 241px; top: 60px;
    width: 294px; height: 30px;
    background: var(--brand-green);
    display: flex; align-items: center;
    padding-left: 15px;
    color: var(--white);
    font-weight: 800; font-size: 14.6px; letter-spacing: 0.2px;
    white-space: nowrap;
  }

  .contact-list { position: absolute; left: 246px; top: 101px; list-style: none; }
  .contact-item { display: flex; align-items: center; color: var(--ink); white-space: nowrap; }
  .contact-icon { width: 10px; height: 10px; margin-right: 19px; flex: none; }
  .contact-phone { font-weight: 700; font-size: 15px; height: 22px; margin-bottom: 2px; }
  .contact-email, .contact-web { font-weight: 500; font-size: 10.8px; height: 16px; }

  .cover-label {
    position: absolute; left: 726px; top: 106px;
    font-weight: 900; font-size: 24px; letter-spacing: 15.5px;
    color: var(--label);
    white-space: nowrap;
  }
</style>
</head>
<body>
<div class="canvas">
  <section class="signature">
    <div class="brand-name">Brightpath<br>Learning<br>Nook</div>

    <div class="person-badge">DANA MORROW</div>
    <div class="person-role">DIRECTOR &amp; LEAD TUTOR</div>

    <div class="divider"></div>

    <div class="business-banner">BRIGHTPATH LEARNING NOOK</div>

    <ul class="contact-list">
      <li class="contact-item contact-phone">
        <svg class="contact-icon" viewBox="0 0 24 24" aria-hidden="true">
          <path fill="#47b169" d="M6.6 10.8a15.1 15.1 0 0 0 6.6 6.6l2.2-2.2c.3-.3.7-.4 1-.2 1.1.4 2.3.6 3.6.6.6 0 1 .4 1 1V20c0 .6-.4 1-1 1A17 17 0 0 1 3 4c0-.6.4-1 1-1h3.5c.6 0 1 .4 1 1 0 1.3.2 2.5.6 3.6.1.3 0 .7-.2 1z"/>
        </svg>
        01632 960418
      </li>
      <li class="contact-item contact-email">
        <svg class="contact-icon" viewBox="0 0 24 24" aria-hidden="true">
          <rect x="2" y="5" width="20" height="14" fill="#47b169"/>
          <path d="M2 5l10 8 10-8M2 19l7.5-7M22 19l-7.5-7" fill="none" stroke="#ffffff" stroke-width="1.6"/>
        </svg>
        hello@brightpathlearningnook.co.uk
      </li>
      <li class="contact-item contact-web">
        <svg class="contact-icon" viewBox="0 0 24 24" aria-hidden="true">
          <g fill="none" stroke="#47b169" stroke-width="1.8">
            <circle cx="12" cy="12" r="9.5"/>
            <ellipse cx="12" cy="12" rx="4.2" ry="9.5"/>
            <path d="M2.5 12h19M4 7h16M4 17h16"/>
          </g>
        </svg>
        www.brightpathlearningnook.co.uk
      </li>
    </ul>
  </section>

  <div class="cover-label">SOCIAL COVER</div>
</div>
</body>
</html>
```